Visit card

Industry/Entity Type

Health Care

Contact Information for Business Card

O VITALE SYSTEMES
Odile Ferrandi - chef de Projet

Requirements
Must have
• 318 Hector Delaunay Street 58210 VERNAUVILLE Tel: 33 (0) 387 419 264 Mobile: 06 42 93 17 58 Web: www.vobelasystems.example Contact: o.ferrandi@o-vitalesystemes.example
Should not have
• Respect for color

```html
<!DOCTYPE html>
<html lang="fr">
<head>
<meta charset="utf-8">
<title>O VITALE SYSTEMES – Carte de visite</title>
<link rel="stylesheet" href="https://fonts.googleapis.com/css2?family=Roboto:wght@400;500;700&display=swap">
<style>
  :root {
    --red: #e02433;
    --red-tint: #f6dfe1;
    --charcoal: #3d3d3f;
    --ink: #2f2f31;
    --paper: #ffffff;
    --page: #e9e7e4;
  }
  * { box-sizing: border-box; margin: 0; padding: 0; }
  html, body { width: 1200px; height: 1021px; overflow: hidden; }
  body {
    background: var(--page);
    font-family: "Roboto", Arial, sans-serif;
    position: relative;
  }
  .card {
    position: absolute;
    left: 220px;
    width: 760px;
    height: 434px;
    border-radius: 4px;
    box-shadow: 0 10px 28px rgba(0,0,0,.18);
    overflow: hidden;
  }
  /* back side */
  .card-back {
    top: 40px;
    background: linear-gradient(180deg, #444446 0%, var(--charcoal) 100%);
  }
  .back-brand {
    position: absolute;
    left: 0; right: 0; top: 150px;
    display: flex; align-items: center; justify-content: center; gap: 18px;
  }
  .brand-dot {
    flex: none;
    width: 30px; height: 30px; border-radius: 50%;
    background: var(--red);
  }
  .back-brand .brand-name {
    color: var(--paper);
    font-weight: 700;
    font-size: 38px;
    letter-spacing: 2px;
  }
  .back-web {
    position: absolute;
    left: 0; right: 0; top: 330px;
    text-align: center;
    color: var(--paper);
    font-size: 17px;
    letter-spacing: 3px;
  }
  .back-web .accent { color: var(--red); }

  /* front side */
  .card-front {
    top: 520px;
    background: var(--paper);
  }
  .front-brand {
    position: absolute;
    left: 44px; top: 44px;
    display: flex; align-items: center; gap: 14px;
  }
  .front-brand .brand-dot { width: 40px; height: 40px; background: var(--charcoal); }
  .front-brand .brand-name {
    color: var(--red);
    font-weight: 700;
    font-size: 30px;
    letter-spacing: 1px;
  }
  .contact {
    position: absolute;
    left: 48px; top: 196px;
    list-style: none;
    color: var(--ink);
    font-size: 19px;
    line-height: 25px;
  }
  .contact li { display: flex; align-items: flex-start; gap: 10px; }
  .contact svg { flex: none; width: 16px; height: 16px; margin-top: 4px; fill: none; stroke: var(--red); stroke-width: 2; }
  .contact .pin { fill: var(--red); stroke: none; }
  .name-band {
    position: absolute;
    right: 0; top: 244px;
    width: 330px; height: 84px;
    background: var(--red-tint);
  }
  .name-tab {
    position: absolute;
    right: 0; top: 312px;
    width: 18px; height: 48px;
    background: var(--red);
    border-radius: 6px 0 0 6px;
  }
  .identity {
    position: absolute;
    right: 40px; top: 254px;
    text-align: right;
  }
  .identity .person { color: var(--red); font-weight: 700; font-size: 28px; }
  .identity .role { color: var(--ink); font-size: 21px; margin-top: 2px; }
</style>
</head>
<body>

<section class="card card-back">
  <div class="back-brand">
    <span class="brand-dot"></span>
    <span class="brand-name">O VITALE SYSTEMES</span>
  </div>
  <p class="back-web">www.<span class="accent">vobelasystems</span>.example</p>
</section>

<section class="card card-front">
  <div class="front-brand">
    <span class="brand-dot"></span>
    <span class="brand-name">O VITALE SYSTEMES</span>
  </div>

  <ul class="contact">
    <li>
      <svg viewBox="0 0 16 16"><path class="pin" d="M8 1a5 5 0 0 0-5 5c0 4 5 9 5 9s5-5 5-9a5 5 0 0 0-5-5zm0 7a2 2 0 1 1 0-4 2 2 0 0 1 0 4z"/></svg>
      <span>318 Hector Delaunay Street<br>58210 VERNAUVILLE</span>
    </li>
    <li>
      <svg viewBox="0 0 16 16"><path d="M4 2l2 3-1.5 1.5a8 8 0 0 0 5 5L11 10l3 2-1 2.5C7 14 2 9 1.5 3z"/></svg>
      <span>+33 (0) 387 419 264</span>
    </li>
    <li>
      <svg viewBox="0 0 16 16"><rect x="4" y="1.5" width="8" height="13" rx="1.5"/><line x1="7" y1="12" x2="9" y2="12"/></svg>
      <span>06 42 93 17 58</span>
    </li>
    <li>
      <svg viewBox="0 0 16 16"><rect x="1.5" y="3.5" width="13" height="9"/><path d="M1.5 3.5L8 9l6.5-5.5"/></svg>
      <span>o.ferrandi@o-vitalesystemes.example</span>
    </li>
    <li>
      <svg viewBox="0 0 16 16"><circle cx="8" cy="8" r="6.5"/><path d="M1.5 8h13M8 1.5c-3 3.5-3 9.5 0 13M8 1.5c3 3.5 3 9.5 0 13"/></svg>
      <span>www.vobelasystems.example</span>
    </li>
  </ul>

  <div class="name-band"></div>
  <div class="name-tab"></div>
  <div class="identity">
    <p class="person">Odile Ferrandi</p>
    <p class="role">chef de Projet</p>
  </div>
</section>

</body>
</html>
```